New Business Card Design Project

Updated business card design. I am moving towards more coaching of, for the most part women, who are searching for more in their lives. I am an intuitive healer, homeopath and nutritionist but also an author and motivational speaker. Int the past I have included my photo on the card but that is not essential. My book is called the Brilliance of Saffron - Reclaiming the Shade of Your Spirit so my colours are typically magenta.
Target Market(s)
Women - 35 - 60 considering improving their health. However, I am also a professional speaker with a target audience including corporate and conferences.
Industry/Entity Type
Health And Wellness
Contact Information for Business Card
Lucinda Parvell, ND, CNP, BSc
www.lucindaparvell.com
lucinda@lucindaparvell.com
519-362-7015
Facebook, instagram and twitter logos
Look and feel
Each slider illustrates characteristics of the customer's brand and the style your logo design should communicate.

```html
<!DOCTYPE html>
<html lang="en">
<head>
<meta charset="utf-8">
<title>Lucinda Parvell – Business Card</title>
<link rel="stylesheet" href="https://fonts.googleapis.com/css2?family=Jost:wght@300;400&family=Lustria&display=swap">
<style>
  :root {
    --backdrop: #2b2b2b;
    --card-dark: #1f1f1f;
    --card-light: #efefef;
    --ink: #2a2a2a;
    --ink-light: #ececec;
    --magenta: #d3326a;
    --photo-dark: #3b2a24;
    --photo-mid: #8a6a5e;
  }
  * { margin: 0; padding: 0; box-sizing: border-box; }
  html, body { width: 1200px; height: 1142px; overflow: hidden; background: var(--backdrop); }
  .canvas { position: relative; width: 1200px; height: 1142px; }

  .card { position: absolute; overflow: hidden; }
  .card-front {
    left: 324px; top: 211px; width: 551px; height: 332px;
    background: var(--card-dark); border-radius: 8px;
  }
  .card-back {
    left: 323px; top: 597px; width: 553px; height: 333px;
    background: var(--card-light); border-radius: 12px;
  }

  .wordmark {
    font-family: "Jost", sans-serif; font-weight: 300;
    white-space: nowrap; line-height: 1;
  }
  .logo-dot { border-radius: 50%; background: var(--magenta); flex: none; }

  .front-logo {
    position: absolute; left: 166px; top: 62px;
    display: flex; flex-direction: column; align-items: flex-start;
  }
  .front-logo .wordmark { font-size: 64px; color: var(--ink-light); }
  .front-logo .line-one { display: flex; align-items: center; gap: 10px; }
  .front-logo .line-two { margin-left: 16px; margin-top: 4px; }
  .front-logo .logo-dot { width: 56px; height: 56px; }

  .tagline {
    font-family: "Jost", sans-serif; font-weight: 300; white-space: nowrap;
    display: flex; align-items: center; justify-content: center;
  }
  .tagline::before, .tagline::after {
    content: ""; width: 7px; height: 7px; border-radius: 50%; background: var(--magenta);
  }
  .front-tagline {
    position: absolute; left: 0; right: 0; top: 230px;
    font-size: 26px; color: var(--ink-light); gap: 14px;
  }

  .portrait {
    position: absolute; left: 0; top: 0; width: 232px; height: 333px;
    background: linear-gradient(160deg, var(--photo-mid) 0%, var(--photo-dark) 55%, #b0365e 100%);
  }

  .back-logo {
    position: absolute; right: 22px; top: 44px;
    display: flex; flex-direction: column; align-items: flex-end;
  }
  .back-logo .mark-row { display: flex; align-items: center; gap: 8px; }
  .back-logo .wordmark { font-size: 36px; color: var(--ink); }
  .back-logo .logo-dot { width: 26px; height: 26px; }
  .back-tagline { font-size: 13px; color: var(--ink); gap: 7px; margin-top: 6px; margin-right: 120px; }
  .back-tagline::before, .back-tagline::after { width: 4px; height: 4px; }

  .person { position: absolute; right: 23px; top: 144px; text-align: right; }
  .person-name { font-family: "Jost", sans-serif; font-weight: 300; font-size: 22px; color: var(--magenta); line-height: 1.1; }
  .person-credentials { font-family: "Lustria", serif; font-size: 11px; color: var(--ink); margin-top: 6px; }

  .contact-list { position: absolute; right: 20px; top: 211px; list-style: none; }
  .contact-list li {
    display: flex; align-items: center; justify-content: flex-end; gap: 9px;
    font-family: "Lustria", serif; font-size: 14px; color: var(--ink); height: 21px;
  }
  .contact-list svg { width: 17px; height: 17px; flex: none; }

  .social-band {
    position: absolute; left: 229px; right: 0; bottom: 0; height: 34px;
    background: var(--magenta); color: #fff;
    display: flex; align-items: center; justify-content: center; gap: 6px;
    font-family: "Jost", sans-serif; font-weight: 300; font-size: 15px; letter-spacing: 0.3px;
  }
  .social-band .follow { margin-right: 4px; }
  .social-dot { width: 16px; height: 16px; border-radius: 50%; background: #fff; flex: none; }
</style>
</head>
<body>
<div class="canvas">

  <section class="card card-front">
    <div class="front-logo">
      <div class="line-one">
        <span class="wordmark">Lucinda</span>
        <span class="logo-dot"></span>
      </div>
      <span class="wordmark line-two">Parvell</span>
    </div>
    <p class="tagline front-tagline">vitality maverick</p>
  </section>

  <section class="card card-back">
    <div class="portrait" role="img" aria-label="Portrait photo of Lucinda Parvell smiling, wearing magenta"></div>

    <div class="back-logo">
      <div class="mark-row">
        <span class="wordmark">Lucinda Parvell</span>
        <span class="logo-dot"></span>
      </div>
      <p class="tagline back-tagline">vitality maverick</p>
    </div>

    <div class="person">
      <p class="person-name">Lucinda Parvell</p>
      <p class="person-credentials">ND, CNP, BSc</p>
    </div>

    <ul class="contact-list">
      <li>519-362-7015
        <svg viewBox="0 0 20 20"><circle cx="10" cy="10" r="8.5" fill="none" stroke="#2a2a2a" stroke-width="1.2"/><path d="M6 8.5q4-3 8 0v1.5h-2v-1h-4v1H6z M7 11h6v3H7z" fill="#d3326a"/></svg>
      </li>
      <li>www.lucindaparvell.com
        <svg viewBox="0 0 20 20"><circle cx="10" cy="10" r="8.5" fill="none" stroke="#2a2a2a" stroke-width="1.2"/><rect x="5.5" y="7" width="9" height="6.5" fill="#d3326a"/><path d="M5.5 7l4.5 3.5L14.5 7" fill="none" stroke="#fff" stroke-width="0.9"/></svg>
      </li>
      <li>lucinda@lucindaparvell.com
        <svg viewBox="0 0 20 20"><circle cx="10" cy="10" r="8.5" fill="none" stroke="#2a2a2a" stroke-width="1.2"/><circle cx="10" cy="10" r="4.5" fill="none" stroke="#d3326a" stroke-width="1.2"/><path d="M5.5 10h9M10 5.5v9" stroke="#d3326a" stroke-width="1"/><ellipse cx="10" cy="10" rx="2" ry="4.5" fill="none" stroke="#d3326a" stroke-width="0.9"/></svg>
      </li>
    </ul>

    <div class="social-band">
      <span class="follow">Follow us on</span>
      <span class="social-dot"></span>
      <span class="social-dot"></span>
      <span class="social-dot"></span>
    </div>
  </section>

</div>
</body>
</html>
```